Bellmoor Commercial Finance Information Brochure

This brochure will be sent out to clients via A4 PDF on an email to showcase what our company has to offer. We are a commercial finance brokerage, that specialises in property finance. We would like to see designs following our colour scheme. The final design should demonstrate our professionalism and reliability.
I have attached our logo and also a few bullet points on our information and what we can offer. These can be slightly reworded for conciseness. Or leave the text sections as filler and I can fill these in.
I have also attached an overview of our colour scheme and design styling for your consideration.
Target Market(s)
Property Developers
Industry/Entity Type
Financial Services

```html
<!DOCTYPE html>
<html lang="en">
<head>
<meta charset="utf-8">
<title>Bellmoor Commercial Finance – Information Brochure</title>
<link href="https://fonts.googleapis.com/css2?family=Roboto:wght@400;500;700&family=Roboto+Condensed:wght@400;700&display=swap" rel="stylesheet">
<style>
  :root{
    --blue:#2c45a3;
    --blue-dark:#22388c;
    --green:#1f8a3e;
    --white:#ffffff;
    --ink:#1d2a5c;
    --stage:#e6e7ea;
    --photo-a:#c9b79a;
    --photo-b:#7a8fa8;
  }
  *{box-sizing:border-box;margin:0;padding:0}
  html,body{width:1200px;height:800px;overflow:hidden}
  body{background:var(--stage);position:relative;font-family:"Roboto Condensed",Arial,sans-serif}
  .sheet{
    position:absolute;left:324px;top:10px;width:595px;height:842px;
    transform:scale(0.926);transform-origin:0 0;
    background:var(--white);overflow:hidden;
    box-shadow:0 6px 18px rgba(0,0,0,.18);
  }
  .shapes{position:absolute;inset:0}
  .wordmark{
    position:absolute;left:24px;top:58px;
    font-family:"Roboto",Arial,sans-serif;font-weight:700;font-size:34px;
    color:var(--blue);letter-spacing:.5px;line-height:1;
  }
  .wordmark-square{position:absolute;left:24px;top:104px;width:12px;height:12px;background:var(--green)}
  .headline{
    position:absolute;left:15px;top:242px;
    font-family:"Roboto",Arial,sans-serif;font-weight:500;font-size:21.5px;line-height:25px;color:var(--white);
  }
  .headline-rule{position:absolute;left:15px;top:308px;width:95px;height:4px;background:var(--green)}
  .copy{position:absolute;color:var(--white);font-size:10.6px;line-height:12px;text-align:justify}
  .copy p+p{margin-top:14px}
  .copy strong{font-weight:700}
  .col-left-a{left:15px;top:322px;width:265px}
  .col-left-b{left:17px;top:478px;width:263px}
  .col-right-a{left:311px;top:327px;width:262px}
  .col-right-b{left:311px;top:476px;width:262px}
  .divider{position:absolute;left:298px;top:275px;width:1px;height:375px;background:rgba(255,255,255,.55)}
  .pill{
    position:absolute;height:28px;width:195px;border-radius:0 14px 14px 14px;
    background:var(--green);color:var(--white);
    font-family:"Roboto",Arial,sans-serif;font-size:12px;
    display:flex;align-items:center;padding-left:32px;
  }
  .pill svg{position:absolute;left:2px;top:2px}
  .pill-apart{left:18px;top:441px}
  .pill-goal{left:305px;top:290px}
  .pill-efficiency{left:305px;top:437px}
  .approach{position:absolute;left:25px;top:666px;width:545px;text-align:center;color:var(--white)}
  .approach h3{font-family:"Roboto",Arial,sans-serif;font-weight:400;font-size:12px;margin-bottom:6px}
  .approach p{font-size:10.6px;line-height:12px}
  .contact{
    position:absolute;left:0;right:0;top:800px;display:flex;justify-content:center;gap:24px;
    font-family:"Roboto",Arial,sans-serif;font-size:12px;color:var(--ink);
  }
  .contact span{display:flex;align-items:center;gap:6px}
</style>
</head>
<body>
  <article class="sheet">
    <svg class="shapes" width="595" height="842" viewBox="0 0 595 842">
      <defs>
        <linearGradient id="siteTones" x1="0" y1="0" x2="0" y2="1">
          <stop offset="0" stop-color="var(--photo-b)"/>
          <stop offset="1" stop-color="var(--photo-a)"/>
        </linearGradient>
      </defs>
      <polygon points="0,148 595,305 595,660 0,640" fill="var(--blue)"/>
      <polygon points="0,150 260,218 0,300" fill="var(--blue-dark)" opacity=".35"/>
      <polygon points="0,640 595,660 595,760 0,770" fill="var(--green)"/>
      <polygon points="330,0 595,0 595,305 220,206" fill="url(#siteTones)" role="img" aria-label="Photo: construction workers in hard hats and hi-vis vests walking on a building site"/>
    </svg>

    <div class="wordmark">Bellmoor Finance</div>
    <div class="wordmark-square"></div>

    <h1 class="headline">WELCOME TO BELLMOOR<br>COMMERCIAL FINANCE</h1>
    <div class="headline-rule"></div>

    <div class="copy col-left-a">
      <p>As former lenders and developers ourselves, we intimately understand the inefficiencies that plague deals in the market today.</p>
      <p>We've experienced the frustration of tight time limits on deals and the exasperating feeling of brokers wasting precious time collecting information. It's enough to drive developers and lenders insane!</p>
    </div>

    <div class="pill pill-apart">
      <svg width="24" height="24" viewBox="0 0 24 24"><circle cx="12" cy="12" r="11" fill="#fff"/><circle cx="12" cy="12" r="5" fill="none" stroke="var(--blue)" stroke-width="2"/></svg>
      WHAT SETS US APART?
    </div>

    <div class="copy col-left-b">
      <p>That's why we founded Bellmoor Finance – to be the efficient and reliable link that connects developers and lenders. We've streamlined our processes to eliminate unnecessary hurdles, enabling clear and swift communication between all parties involved. No more wasted time. No more unnecessary stress.</p>
      <p>With our expertise and industry insights, we've developed a unique approach that simplifies the financing journey. From the initial consultation to the final funding, we're here to guide you every step of the way.</p>
    </div>

    <div class="divider"></div>

    <div class="pill pill-goal">
      <svg width="24" height="24" viewBox="0 0 24 24"><circle cx="12" cy="12" r="11" fill="#fff"/><circle cx="12" cy="12" r="6" fill="none" stroke="var(--blue)" stroke-width="2"/><circle cx="12" cy="12" r="2" fill="var(--green)"/></svg>
      OUR GOAL?
    </div>

    <div class="copy col-right-a">
      <p><strong>To make commercial financing a smooth and enjoyable experience for you.</strong> With our background in the asset management industry, we have cultivated a black book of fund managers, institutions, UHNWI and private equity lenders that we can call on for non-traditional lending. Bellmoor Finance was created to satisfy a need in the market that has been far too overlooked.</p>
    </div>

    <div class="pill pill-efficiency">
      <svg width="24" height="24" viewBox="0 0 24 24"><circle cx="12" cy="12" r="11" fill="#fff"/><circle cx="12" cy="12" r="6" fill="none" stroke="var(--blue)" stroke-width="2" stroke-dasharray="3 2"/><circle cx="12" cy="12" r="2.5" fill="var(--green)"/></svg>
      EFFICIENCY.
    </div>

    <div class="copy col-right-b">
      <p>Efficiency is at the heart of our operations, and we pride ourselves on our ability to secure the best financing options swiftly and effectively for our clients. By employing cutting-edge technology and streamlining our internal processes, we have cultivated a seamless and time-saving approach to finance brokering.</p>
      <p>Having been a developer, we understand the stresses and headaches associated with building, let alone all the paperwork and emails backwards and forwards between yourself and brokers to attain the necessary financing.</p>
    </div>

    <section class="approach">
      <h3>OUR APPROACH.</h3>
      <p>We are well-versed in the questions lenders will ask, allowing us to get ahead of the curve and request all the necessary information from you on day one. This approach provides you with a distinct advantage, as it eliminates the need to allocate hours each day to answering questions and fulfilling requests from brokers. By entrusting us with this responsibility, you can focus on your core tasks and leave the financing aspect to us, making the process less stressful for you.</p>
    </section>

    <footer class="contact">
      <span><svg width="12" height="12" viewBox="0 0 12 12"><circle cx="6" cy="6" r="6" fill="var(--green)"/><rect x="3" y="4" width="6" height="4" fill="#fff"/></svg>enquiries@bellmoorfinance.co.uk</span>
      <span><svg width="12" height="12" viewBox="0 0 12 12"><circle cx="6" cy="6" r="5.3" fill="none" stroke="var(--green)" stroke-width="1.3"/><path d="M4 3.5 L5 3.5 L5.5 5 L5 5.5 Q5.6 6.6 6.5 7 L7 6.5 L8.5 7 L8.5 8 Q5 8.5 4 3.5Z" fill="var(--green)"/></svg>0800 046 2190</span>
      <span><svg width="12" height="12" viewBox="0 0 12 12"><circle cx="6" cy="6" r="5.3" fill="none" stroke="var(--green)" stroke-width="1.3"/><circle cx="6" cy="6" r="2.5" fill="none" stroke="var(--green)" stroke-width="1"/></svg>www.bellmoorfinance.co.uk</span>
    </footer>
  </article>
</body>
</html>
```